VeLT Record Shredding professional postcard

I'm looking for a postcard design that tells a story in very few words about how important it is to protect yourself your family and your clients against sensitive information and identity theft. My website is veltrecordshredding.net if you are looking for text to put on card. Would like "secure and certified destruction of your data and media" on the postcard.

Target Market(s)

Commercial and residential.

Industry/Entity Type

Business Service

Font styles to use
Serif

Colors
000000

Requirements
Must have
• A pic, 1-855-318-4096 phone number, veltrecordshredding.net web address area for postage must be double sided. Definitely want it eye catching. Must have an area for postage and mailing address. Would like to see glossy on one side and the other side not glossy

```html
<!DOCTYPE html>
<html lang="en">
<head>
<meta charset="utf-8">
<title>VeLT Record Shredding – Postcard</title>
<link rel="stylesheet" href="https://fonts.googleapis.com/css2?family=Marcellus&family=Crimson+Pro:wght@400;700&family=Open+Sans:wght@400;700&display=swap">
<style>
  :root {
    --page-bg: #e9e9e7;
    --brand-green: #3fa34d;
    --brand-blue: #2b5fa6;
    --badge-teal: #0f6b63;
    --photo-dark: #1b1b1d;
    --photo-mid: #4a4446;
    --white: #ffffff;
    --ink: #1f1f1f;
    --stamp-grey: #e4e4e4;
  }
  * { box-sizing: border-box; margin: 0; padding: 0; }
  html, body { width: 1200px; height: 640px; overflow: hidden; }
  body { background: var(--page-bg); position: relative; font-family: "Open Sans", sans-serif; }

  .postcard {
    position: absolute; top: 154px; width: 514px; height: 332px; overflow: hidden;
    box-shadow: 0 4px 10px rgba(0,0,0,.25);
  }
  .postcard--front { left: 59px; background: var(--photo-dark); }
  .postcard--back { left: 626px; background: var(--white); }

  /* front */
  .front-photo {
    position: absolute; inset: 0;
    background: linear-gradient(100deg, #3a2e2f 0%, #4b3c3d 30%, #141416 42%, #5a5a5e 65%, #222226 85%, #0f0f10 100%);
  }
  .front-bands { position: absolute; inset: 0; }
  .front-logo {
    position: absolute; left: 1px; top: -14px; width: 152px; height: 152px; border-radius: 50%;
    background: rgba(255,255,255,.28); display: flex; align-items: center; justify-content: center;
  }
  .front-logo__ring {
    width: 128px; height: 128px; border-radius: 50%; background: rgba(255,255,255,.45);
    display: flex; align-items: center; justify-content: center;
  }
  .front-logo__disc {
    width: 108px; height: 108px; border-radius: 50%; background: var(--white);
    display: flex; align-items: center; justify-content: center; text-align: center;
  }
  .brand-name {
    font-family: "Marcellus", serif; color: var(--brand-blue); font-size: 13px; line-height: 1.2;
  }
  .front-headline {
    position: absolute; left: 165px; top: 44px; color: var(--white);
    font-family: "Marcellus", serif; line-height: 1.1;
  }
  .front-headline__top { font-size: 16px; letter-spacing: .3px; }
  .front-headline__main { font-size: 24px; }
  .front-headline__of { font-size: 15px; }
  .cert-badge { position: absolute; border-radius: 50%; background: var(--badge-teal); border: 2px solid var(--white); }
  .postcard--front .cert-badge { left: 417px; top: 114px; width: 84px; height: 84px; }
  .front-contacts { position: absolute; left: 230px; top: 254px; list-style: none; }
  .front-contacts li {
    display: flex; align-items: center; gap: 7px; height: 24px;
    font-family: "Crimson Pro", serif; font-weight: 700; font-size: 17px; color: var(--white);
  }
  .contact-icon { width: 15px; height: 15px; flex: none; }

  /* back */
  .back-brand { position: absolute; left: 30px; top: 32px; width: 110px; }
  .back-headline {
    position: absolute; left: 22px; top: 102px; font-family: "Marcellus", serif;
    color: var(--brand-blue); font-size: 15px; line-height: 18px; font-weight: 700; letter-spacing: .2px;
  }
  .back-contacts { position: absolute; left: 22px; top: 176px; list-style: none; }
  .back-contacts li {
    display: flex; align-items: center; gap: 5px; height: 20px;
    font-family: "Crimson Pro", serif; font-size: 12px; color: var(--brand-green);
  }
  .back-contacts .contact-icon { width: 10px; height: 10px; }
  .postcard--back .cert-badge { left: 22px; top: 250px; width: 58px; height: 58px; border-width: 1.5px; }
  .postage-stamp {
    position: absolute; left: 406px; top: 22px; width: 77px; height: 76px; background: var(--stamp-grey);
    display: flex; align-items: center; justify-content: center; text-align: center;
    font-family: "Crimson Pro", serif; font-weight: 700; font-size: 7px; line-height: 1.1; color: var(--ink);
  }
  .mailing-address {
    position: absolute; left: 285px; top: 194px; font-size: 6.5px; line-height: 1.35; color: var(--ink);
  }
  .mailing-address p + p { margin-top: 0; }
  .mailing-address .mailing-address__contact { margin-top: 7px; }
</style>
</head>
<body>

<section class="postcard postcard--front" aria-label="Postcard front">
  <div class="front-photo" role="img" aria-label="Photo of an industrial media shredder beside an opened hard drive"></div>
  <svg class="front-bands" viewBox="0 0 514 332" width="514" height="332" aria-hidden="true">
    <polygon points="0,0 514,0 514,100 0,136" fill="var(--brand-green)"/>
    <polygon points="0,140 514,102 514,106 0,144" fill="var(--brand-blue)"/>
    <polygon points="0,150 514,112 514,113.5 0,151.5" fill="var(--brand-green)"/>
  </svg>
  <div class="front-logo">
    <div class="front-logo__ring">
      <div class="front-logo__disc"><span class="brand-name">VeLT Record<br>Shredding</span></div>
    </div>
  </div>
  <h1 class="front-headline">
    <span class="front-headline__top">SECURE AND CERTIFIED DESTRUCTION</span><br>
    <span class="front-headline__of">OF </span><span class="front-headline__main">YOUR DATA AND MEDIA</span>
  </h1>
  <div class="cert-badge" role="img" aria-label="Certification badge"></div>
  <ul class="front-contacts">
    <li>
      <svg class="contact-icon" viewBox="0 0 16 16"><circle cx="8" cy="8" r="8" fill="var(--badge-teal)"/><path d="M5.3 4.2l1.4 1.6-.8 1a5 5 0 0 0 2.4 2.4l1-.8 1.6 1.4-.8 1.2C7.6 11 5 8.4 4.1 5z" fill="none" stroke="#fff" stroke-width=".8"/></svg>
      1-855-318-4096
    </li>
    <li>
      <svg class="contact-icon" viewBox="0 0 16 16"><circle cx="8" cy="8" r="8" fill="var(--badge-teal)"/><circle cx="7.3" cy="7.3" r="2.8" fill="none" stroke="#fff" stroke-width=".9"/><path d="M9.3 9.3l2.3 2.3" stroke="#fff" stroke-width=".9"/></svg>
      www.veltrecordshredding.net
    </li>
  </ul>
</section>

<section class="postcard postcard--back" aria-label="Postcard back">
  <div class="back-brand"><span class="brand-name">VeLT Record Shredding</span></div>
  <h2 class="back-headline">SECURE AND CERTIFIED<br>DESTRUCTION OF<br>YOUR DATA AND MEDIA</h2>
  <ul class="back-contacts">
    <li>
      <svg class="contact-icon" viewBox="0 0 16 16"><path d="M4 2l2.4 2.6-1.3 1.7a8 8 0 0 0 4.6 4.6l1.7-1.3L14 12l-1.4 2C7.6 13.4 2.6 8.4 2 3.4z" fill="none" stroke="var(--brand-green)" stroke-width="1.2"/></svg>
      1-855-318-4096
    </li>
    <li>
      <svg class="contact-icon" viewBox="0 0 16 16"><circle cx="7" cy="7" r="5" fill="none" stroke="var(--brand-green)" stroke-width="1.4"/><path d="M10.6 10.6L14.5 14.5" stroke="var(--brand-green)" stroke-width="1.4"/></svg>
      www.veltrecordshredding.net
    </li>
  </ul>
  <div class="cert-badge" role="img" aria-label="Certification badge"></div>
  <div class="postage-stamp">POSTAGE<br>STAMP</div>
  <address class="mailing-address">
    <p>LOREM IPSUM DOLOR SIT</p>
    <p>Lorem ipsum dolor sit amet lorem ipsum dolor sit amet</p>
    <p>Address, Street name, #409</p>
    <p>City, Other Info</p>
    <p class="mailing-address__contact">Contact No. 000 000 0000</p>
  </address>
</section>

</body>
</html>
```